Bref créative
Retro design logo for building Materials company
R.K. Morrow Company
Professional
Peter K. Morrow
Certified Builder
342 Ferngate Lane, Unit 4
Cedar Hollow, OK 72814
pmorrow@buildwiseterra.com
This is my logo AI file.

```html
<!DOCTYPE html>
<html lang="en">
<head>
<meta charset="utf-8">
<title>R.K. Morrow Company – Business Card</title>
<link href="https://fonts.googleapis.com/css2?family=Cinzel:wght@500&family=Open+Sans:wght@400;700&display=swap" rel="stylesheet">
<style>
  :root {
    --backdrop: #e8e4da;
    --card: #0c0c0c;
    --ink: #ffffff;
    --muted: #cfcfcf;
    --band: #3a3a3a;
    --silver-light: #f2f2f2;
    --silver-dark: #8c8c8c;
  }
  * { margin: 0; padding: 0; box-sizing: border-box; }
  html, body { width: 1200px; height: 398px; overflow: hidden; background: var(--backdrop); }
  .canvas { position: relative; width: 1200px; height: 398px; }
  .card {
    position: absolute; top: 39px; width: 560px; height: 320px;
    background: var(--card); border-radius: 16px; overflow: hidden;
    box-shadow: 0 4px 10px rgba(0,0,0,.25);
  }
  .card--front { left: 24px; }
  .card--back { left: 616px; }

  .brand { position: absolute; left: 0; top: 42px; width: 300px; text-align: center; }
  .brand__mark {
    width: 86px; height: 86px; margin: 0 auto 18px;
    border: 5px solid var(--ink); border-radius: 50%;
  }
  .brand__name {
    font-family: "Cinzel", serif; font-weight: 500; color: var(--ink);
    font-size: 24px; letter-spacing: 1px; white-space: nowrap;
  }

  .divider { position: absolute; left: 356px; top: 100px; width: 1px; height: 118px; background: #6a6a6a; }

  .contact {
    position: absolute; left: 370px; top: 100px;
    font-family: "Open Sans", sans-serif; color: var(--muted); font-size: 10.5px; line-height: 18px;
    list-style: none;
  }
  .contact__item { display: flex; align-items: center; gap: 7px; white-space: nowrap; }
  .contact__item svg { width: 10px; height: 10px; fill: var(--muted); flex: none; }
  .contact__address { margin-top: 12px; padding-left: 17px; white-space: nowrap; }

  .swoosh { position: absolute; left: 0; bottom: 0; width: 560px; height: 110px; }

  .person {
    position: absolute; right: 28px; bottom: 22px; text-align: right;
    font-family: "Open Sans", sans-serif; color: var(--ink);
  }
  .person__name { font-weight: 700; font-size: 17px; line-height: 22px; }
  .person__credential { font-size: 11px; line-height: 15px; color: var(--muted); letter-spacing: .5px; }

  .back-brand {
    position: absolute; inset: 0; display: flex; flex-direction: column;
    align-items: center; justify-content: center;
  }
  .back-brand__mark {
    width: 170px; height: 170px; border: 10px solid var(--ink); border-radius: 50%;
    margin-bottom: 22px;
  }
  .back-brand__name {
    font-family: "Cinzel", serif; font-weight: 500; color: var(--ink);
    font-size: 26px; letter-spacing: 1px; white-space: nowrap;
  }
</style>
</head>
<body>
<main class="canvas">
  <section class="card card--front" aria-label="Card front">
    <div class="brand">
      <div class="brand__mark"></div>
      <p class="brand__name">R.K. MORROW Co.</p>
    </div>

    <div class="divider"></div>

    <ul class="contact">
      <li class="contact__item">
        <svg viewBox="0 0 12 12" aria-hidden="true"><rect x="3" y="0.5" width="6" height="11" rx="1.2"/></svg>
        418-555-0142
      </li>
      <li class="contact__item">
        <svg viewBox="0 0 12 12" aria-hidden="true"><path d="M0 2h12v8H0z M0.8 2.6 6 6.6l5.2-4H0.8z" fill-rule="evenodd"/></svg>
        pmorrow@buildwiseterra.com
      </li>
      <li class="contact__address">342 Ferngate Lane, Unit 4<br>Cedar Hollow, OK 72814</li>
    </ul>

    <svg class="swoosh" viewBox="0 0 560 110" preserveAspectRatio="none" aria-hidden="true">
      <defs>
        <linearGradient id="silver" x1="0" y1="0" x2="1" y2="0">
          <stop offset="0" stop-color="#8c8c8c"/>
          <stop offset=".45" stop-color="#f2f2f2"/>
          <stop offset="1" stop-color="#8c8c8c"/>
        </linearGradient>
      </defs>
      <path d="M0 40 C140 95 300 10 560 30 L560 110 L0 110 Z" fill="url(#silver)"/>
      <path d="M0 62 C160 105 320 40 560 50 L560 110 L0 110 Z" fill="#3a3a3a"/>
      <path d="M0 52 C150 100 310 28 560 41" fill="none" stroke="#ffffff" stroke-width="1.2" opacity=".7"/>
    </svg>

    <div class="person">
      <p class="person__name">Peter K. Morrow</p>
      <p class="person__credential">Certified Builder</p>
    </div>
  </section>

  <section class="card card--back" aria-label="Card back">
    <div class="back-brand">
      <div class="back-brand__mark"></div>
      <p class="back-brand__name">R.K. MORROW Co.</p>
    </div>
  </section>
</main>
</body>
</html>
```